Income Tax Business Cards - Updates

Need to update these business cards while keeping all the same wording but just update them and make them look nicer and more modern/ on brand with our brand.

Industry/Entity Type

finance

Contact Information for Business Card

we have multiple locations so will just need to easily be able to change the address and phone numbers

Colors

Designer to choose colors to be used in the design.

```html
<!DOCTYPE html>
<html lang="en">
<head>
<meta charset="utf-8">
<title>Meridian Financial – Tax Business Cards</title>
<link rel="stylesheet" href="https://fonts.googleapis.com/css2?family=Crimson+Text:ital,wght@0,400;0,600;0,700;1,600;1,700&display=swap">
<style>
  :root {
    --brand-red: #bb2229;
    --brand-green: #174d2d;
    --card-white: #ffffff;
    --ink: #1c1c1c;
    --page-bg: #f1f1f3;
  }
  html, body {
    margin: 0;
    padding: 0;
    width: 1200px;
    height: 1200px;
    overflow: hidden;
    background: var(--page-bg);
  }
  .canvas {
    position: relative;
    width: 1200px;
    height: 1200px;
    font-family: "Crimson Text", Georgia, serif;
  }
  .card {
    position: absolute;
    left: 244px;
    width: 712px;
    display: block;
  }
  .card--front { top: 152px; height: 398px; }
  .card--back  { top: 619px; height: 406px; }
  .fill-white { fill: var(--card-white); }
  .fill-red { fill: var(--brand-red); }
  .fill-green { fill: var(--brand-green); }
  .card text { font-family: "Crimson Text", Georgia, serif; }
  .brand-name { fill: var(--brand-green); font-weight: 600; font-size: 27px; }
  .contact-phone { fill: var(--ink); font-size: 15px; }
  .contact-line { fill: var(--ink); font-size: 13.5px; }
  .offer-upto { fill: var(--card-white); font-style: italic; font-weight: 600; font-size: 36px; }
  .offer-amount { fill: var(--card-white); font-weight: 600; font-size: 70px; }
  .offer-label { fill: var(--card-white); font-weight: 700; font-size: 18px; }
  .offer-note { fill: var(--card-white); font-style: italic; font-weight: 700; font-size: 8.5px; }
  .band-cta { fill: var(--card-white); font-weight: 700; font-size: 18px; letter-spacing: 0.5px; }
  .headline-small { fill: var(--brand-green); font-weight: 700; font-size: 37px; }
  .headline-large { fill: var(--brand-green); font-weight: 700; font-size: 51px; }
  .promo-upto { fill: var(--brand-red); font-style: italic; font-weight: 700; font-size: 38px; }
  .promo-amount { fill: var(--brand-red); font-style: italic; font-weight: 700; font-size: 78px; }
  .promo-label { fill: var(--brand-green); font-weight: 700; font-size: 22px; }
</style>
</head>
<body>
<main class="canvas">

  <!-- Front of card -->
  <svg class="card card--front" viewBox="0 0 526 294" aria-label="Business card front">
    <defs>
      <clipPath id="front-shape"><rect width="526" height="294" rx="20" ry="20"/></clipPath>
    </defs>
    <g clip-path="url(#front-shape)">
      <rect class="fill-white" width="526" height="294"/>
      <polygon class="fill-green" points="355,0 368,0 196,258 183,258"/>
      <polygon class="fill-red" points="368,0 526,0 526,258 196,258"/>
      <rect class="fill-green" x="0" y="264" width="526" height="30"/>
      <polygon class="fill-white" points="271,264 280,264 260,294 251,294"/>
    </g>

    <text class="brand-name" x="128" y="112" text-anchor="middle">Meridian Financial</text>

    <text class="contact-phone" x="127" y="170" text-anchor="middle">(555)555-5555</text>
    <text class="contact-line" x="126" y="193" text-anchor="middle">Adress Line 1</text>
    <text class="contact-line" x="126" y="211" text-anchor="middle">Adress Line 2</text>
    <text class="contact-line" x="126" y="229" text-anchor="middle">Adress Line 3</text>

    <text class="offer-upto" x="497" y="95" text-anchor="end">UP TO</text>
    <text class="offer-amount" x="497" y="153" text-anchor="end">$6,000</text>
    <text class="offer-label" x="498" y="191" text-anchor="end">SAME DAY ADVANCE</text>
    <text class="offer-note" x="498" y="210" text-anchor="end">ON APPROVED TAX RETURNS!</text>

    <text class="band-cta" x="400" y="288" text-anchor="middle">FREE&#160; ESTIMATE!</text>
  </svg>

  <!-- Back of card -->
  <svg class="card card--back" viewBox="0 0 526 300" aria-label="Business card back">
    <defs>
      <clipPath id="back-shape"><rect width="526" height="300" rx="20" ry="20"/></clipPath>
    </defs>
    <g clip-path="url(#back-shape)">
      <rect class="fill-white" width="526" height="300"/>
      <rect class="fill-green" x="0" y="0" width="526" height="36"/>
      <polygon class="fill-white" points="276,0 285,0 264,36 255,36"/>
      <rect class="fill-green" x="0" y="263" width="526" height="37"/>
      <polygon class="fill-white" points="276,263 285,263 264,300 255,300"/>

      <g class="arrow arrow--left">
        <rect class="fill-red" x="0" y="168" width="30" height="24"/>
        <polygon class="fill-red" points="28,157 53,180 28,203"/>
      </g>
      <g class="arrow arrow--right">
        <rect class="fill-red" x="496" y="168" width="30" height="24"/>
        <polygon class="fill-red" points="498,157 473,180 498,203"/>
      </g>
    </g>

    <text class="headline-small" x="263" y="78" text-anchor="middle">FILE YOUR</text>
    <text class="headline-large" x="263" y="128" text-anchor="middle">TAXES HERE</text>
    <text class="promo-upto" x="72" y="194">UP TO</text>
    <text class="promo-amount" x="225" y="204">$6,000</text>
    <text class="promo-label" x="263" y="244" text-anchor="middle">SAME DAY ADVANCE</text>
  </svg>

</main>
</body>
</html>
```